Halcyon Glide Door Product info

Need a catalog designed. 4 -6 pages
We are a commercial sliding door company.
Primary product is a barn door
35 STC Rating (sound rating)
see our web pages listed below
www.halcyonglidedoor.example
www.quickbarsupply.example
Our product is gaining huge strides throughout the medical and hospitality sectors.
this is a 4- 6 page catalogue / brochure . Our product is currently used in many places but we also are creating new markets in the office space.
Updates

Target Market(s)

Commercial Architects , designers , Contractors .
Hospitals , high end hotels , Commercial building planners

Industry/Entity Type

Construction Company

Font styles to use
Serif

Requirements
Must have
• Selling points as to why our product is superior, good flow from concept to end. catch the eye of a designer . technical info . info on sound rating , Good photos, will provide better photos.
Nice to have
• see website from meridel doors and see ideas
Should not have
• too much writing

```html
<!DOCTYPE html>
<html lang="en">
<head>
<meta charset="utf-8">
<title>Halcyon Glide Door – Catalogue Covers</title>
<link rel="stylesheet" href="https://fonts.googleapis.com/css2?family=Open+Sans:wght@400;600;700&display=swap">
<style>
  :root {
    --bg: #b7d2dc;
    --navy: #33608f;
    --navy-light: #3f70a3;
    --band: #3e4b68;
    --paper: #f7f9fc;
    --paper-shade: #e9eef5;
    --accent: #2f6aa3;
    --ink: #2b3445;
    --muted: #5b6577;
    --white: #ffffff;
  }
  * { box-sizing: border-box; margin: 0; padding: 0; }
  html, body { width: 1200px; height: 789px; overflow: hidden; }
  body {
    background: var(--bg);
    font-family: "Open Sans", Arial, sans-serif;
    display: flex;
    align-items: center;
    justify-content: center;
  }
  .spread { display: flex; width: 1000px; height: 707px; box-shadow: 0 10px 30px rgba(40,70,90,.25); }
  .page { position: relative; width: 500px; height: 707px; overflow: hidden; }

  /* Back cover */
  .back-cover {
    background: linear-gradient(160deg, var(--navy-light) 0%, var(--navy) 55%, #2d5784 100%);
    color: var(--white);
    text-align: center;
  }
  .back-cover .tagline {
    position: absolute; top: 268px; left: 50%; transform: translateX(-50%);
    border: 1px solid rgba(255,255,255,.55);
    padding: 12px 26px;
    font-size: 22px; letter-spacing: 1.5px; white-space: nowrap;
  }
  .contact-title {
    position: absolute; top: 352px; left: 0; right: 0;
    font-size: 16px; font-weight: 700; letter-spacing: .5px;
  }
  .contact-title::after {
    content: ""; display: block; width: 150px; height: 1px;
    background: rgba(255,255,255,.55); margin: 10px auto 0;
  }
  .contact-list { position: absolute; top: 400px; left: 0; right: 0; list-style: none; }
  .contact-list li { margin-bottom: 12px; font-size: 12.5px; letter-spacing: .3px; }
  .contact-icon {
    display: block; width: 22px; height: 22px; margin: 0 auto 5px;
    border: 1px solid rgba(255,255,255,.8); border-radius: 50%;
  }
  .contact-icon svg { width: 12px; height: 12px; margin-top: 4px; }
  .band {
    position: absolute; left: 0; right: 0; bottom: 0; height: 40px;
    background: var(--band); color: var(--white);
    display: flex; align-items: center; justify-content: center;
    font-size: 14px; letter-spacing: 1px;
  }

  /* Front cover */
  .front-cover { background: linear-gradient(170deg, var(--white) 0%, var(--paper) 60%, var(--paper-shade) 100%); color: var(--ink); }
  .brand { position: absolute; top: 66px; left: 0; right: 0; text-align: center; }
  .brand-name {
    display: inline-flex; align-items: center; gap: 10px;
    font-size: 26px; font-weight: 600; color: var(--ink); letter-spacing: 1px;
  }
  .brand-mark { width: 12px; height: 12px; border-radius: 50%; background: var(--accent); }
  .brand-sub { font-size: 12px; color: var(--muted); letter-spacing: 1px; margin-top: 4px; }
  .hero-photo {
    position: absolute; top: 160px; left: 36px; right: 0; height: 230px;
    background: linear-gradient(90deg, #6d7a86 0%, #a59a85 45%, #7c7f86 70%, #c9ccd2 100%);
  }
  .slogan {
    position: absolute; top: 412px; right: 30px;
    font-size: 16px; font-weight: 700; color: var(--accent); letter-spacing: .5px;
  }
  .intro-box {
    position: absolute; top: 452px; left: 46px; right: 30px; height: 70px;
    border: 1px solid #9aa9be;
    text-align: center; padding-top: 10px;
    font-size: 17px; color: var(--ink); line-height: 1.4; letter-spacing: .5px;
  }
  .intro-note {
    position: absolute; top: 536px; left: 0; right: 30px; text-align: right;
    font-size: 10.5px; color: var(--muted);
  }
  .front-cover .band { font-size: 13px; height: 38px; bottom: 30px; }
</style>
</head>
<body>
  <main class="spread">
    <section class="page back-cover">
      <p class="tagline">Quality without compromise.</p>
      <h2 class="contact-title">Contact Us:</h2>
      <ul class="contact-list">
        <li>
          <span class="contact-icon"><svg viewBox="0 0 24 24" fill="#fff"><path d="M6.6 10.8a15 15 0 0 0 6.6 6.6l2.2-2.2c.3-.3.7-.4 1-.2 1.1.4 2.3.6 3.6.6.6 0 1 .4 1 1V20c0 .6-.4 1-1 1A17 17 0 0 1 3 4c0-.6.4-1 1-1h3.5c.6 0 1 .4 1 1 0 1.3.2 2.5.6 3.6.1.3 0 .7-.2 1z"/></svg></span>
          555-014-2290
        </li>
        <li>
          <span class="contact-icon"><svg viewBox="0 0 24 24" fill="none" stroke="#fff" stroke-width="2"><rect x="3" y="5" width="18" height="14"/><path d="M3 5l9 8 9-8"/></svg></span>
          sales@quickbarsupply.example
        </li>
        <li>
          <span class="contact-icon"><svg viewBox="0 0 24 24" fill="none" stroke="#fff" stroke-width="2"><circle cx="12" cy="12" r="9"/><path d="M3 12h18M12 3c3 3 3 15 0 18M12 3c-3 3-3 15 0 18"/></svg></span>
          www.halcyonglidedoor.example
        </li>
      </ul>
      <footer class="band">Copyright © Halcyon Glide Doors. All Right Reserved.</footer>
    </section>

    <section class="page front-cover">
      <header class="brand">
        <div class="brand-name"><span class="brand-mark"></span>Halcyon</div>
        <p class="brand-sub">Sliding Door Systems</p>
      </header>
      <div class="hero-photo" role="img" aria-label="Photo of a hotel corridor with glass wall and acoustic sliding doors"></div>
      <p class="slogan">Sound.... Sealed.... Delivered....</p>
      <div class="intro-box">We are<br>a commercial sliding door company.</div>
      <p class="intro-note">The best performing sliding door out there, without any compromise.</p>
      <footer class="band">www.halcyonglidedoor.example</footer>
    </section>
  </main>
</body>
</html>
```